Personal Grocery Shopping Webpage Design

We need a home webpage for a local neighborhood grocery delivery website called "Thornwick Personal Grocery Shopping & Delivery". We would like to use a color scheme of Grape or Purple and Gray. We would like for the website to have a basic menu bar that includes Home/About Us; Grocery Items; How to Order. we would like to include the uploaded text on the home page. we would like for the website to communicate that this is a personal grocery shopping valet service geared toward upscale customers. The Halvern Moreau for personal grocery shopping

```html
<!DOCTYPE html>
<html lang="en">
<head>
<meta charset="utf-8">
<title>Thornwick Delivery</title>
<link href="https://fonts.googleapis.com/css2?family=Lato:wght@300;400;700&display=swap" rel="stylesheet">
<style>
:root{
  --grape:#9c3f95;
  --grape-light:#b758ae;
  --ink:#333333;
  --muted:#8a8a8a;
  --gray-band:#f3f3f3;
  --line:#e2e2e2;
  --white:#ffffff;
}
*{box-sizing:border-box;margin:0;padding:0}
html,body{width:1200px;height:2683px;overflow:hidden}
body{font-family:'Lato',Arial,sans-serif;color:var(--ink);background:var(--white);position:relative}
.abs{position:absolute}
.center{text-align:center;left:0;right:0}

.topbar{top:0;left:0;width:1200px;height:32px;background:var(--grape);color:var(--white);font-size:11px;font-weight:700;letter-spacing:.5px;display:flex;align-items:center;padding-left:132px;gap:18px}
.topbar span{display:flex;align-items:center;gap:6px}
.header{top:32px;left:0;width:1200px;height:111px;background:var(--white)}
.brand{left:132px;top:36px;font-size:30px;color:var(--grape);font-weight:700;letter-spacing:.3px}
.account{right:132px;top:30px;font-size:11px;letter-spacing:1px;color:#555;display:flex;gap:18px;align-items:center}
.nav{right:125px;top:78px;display:flex;gap:42px;font-size:11px;color:#333;letter-spacing:.3px}
.nav .active{color:var(--grape);position:relative}
.nav .active::after{content:"";position:absolute;left:-4px;right:-4px;bottom:-14px;height:2px;background:var(--grape)}

.hero{top:143px;left:0;width:1200px;height:465px;background:radial-gradient(ellipse at 30% 55%,#7a4a2a 0%,#4a2a18 40%,#241610 75%,#1a110c 100%)}
.hero-title{top:130px;font-size:40px;color:var(--white);font-weight:400;letter-spacing:1px}
.hero-sub{top:212px;font-size:15px;color:#f2f2f2}
.btn-hero{top:279px;left:527px;width:145px;height:43px;background:var(--grape-light);color:var(--white);font-size:14px;display:flex;align-items:center;justify-content:center;border-radius:3px}
.dots{top:414px;left:578px;display:flex;gap:6px}
.dots i{width:9px;height:9px;border-radius:50%;background:#ddd;display:block}
.dots i:first-child{background:var(--grape-light)}

.sec-title{font-size:34px;font-weight:400;color:var(--ink);letter-spacing:.5px}
.intro{top:738px;left:250px;width:700px;font-size:10.5px;line-height:24px;color:var(--muted);text-align:center}
.feature{width:300px;text-align:center}
.feature .icon{width:122px;height:122px;border-radius:50%;background:var(--grape);margin:0 auto;display:flex;align-items:center;justify-content:center}
.feature h3{margin-top:50px;font-size:18px;font-weight:400;letter-spacing:.3px}
.feature p{margin-top:30px;font-size:10.5px;line-height:24px;color:var(--muted);padding:0 12px}

.order-band{top:1198px;left:0;width:1200px;height:510px;background:var(--gray-band)}
.step{width:300px;text-align:center}
.step .photo{width:194px;height:194px;border-radius:50%;margin:0 auto;border:3px solid var(--white)}
.step h4{margin-top:40px;font-size:18px;font-weight:400;letter-spacing:.3px}

.product{width:217px}
.product .photo{height:274px}
.product h5{margin-top:26px;font-size:18px;font-weight:400}
.product .price{margin-top:16px;font-size:19px}
.product .add{margin-top:16px;width:129px;height:38px;background:var(--grape-light);color:var(--white);font-size:11px;letter-spacing:1px;display:flex;align-items:center;justify-content:center;border-radius:2px}

.footer{top:2383px;left:0;width:1200px;height:236px;background:var(--gray-band)}
.foot-brand{left:127px;top:38px;font-size:28px;color:var(--grape);font-weight:700}
.social{left:132px;top:86px;display:flex;gap:8px}
.social i{width:30px;height:30px;border-radius:50%;border:1.5px solid #666;display:block}
.col{top:38px}
.col h6{font-size:19px;font-weight:400;letter-spacing:2px;color:#333}
.col ul{list-style:none;margin-top:20px}
.col li{font-size:11px;color:#555;height:24px;display:flex;align-items:center;gap:10px}
.copyright{top:2619px;left:0;width:1200px;height:64px;display:flex;align-items:center;justify-content:center;font-size:11px;color:#777;border-top:1px solid var(--line)}
</style>
</head>
<body>

<div class="abs topbar">
  <span>SIMPLY TEXT YOUR ORDER</span>
  <span><svg width="11" height="11" viewBox="0 0 24 24"><path fill="#fff" d="M6.6 10.8a15 15 0 0 0 6.6 6.6l2.2-2.2c.3-.3.7-.4 1-.2 1.1.4 2.3.6 3.6.6.6 0 1 .4 1 1V20c0 .6-.4 1-1 1A17 17 0 0 1 3 4c0-.6.4-1 1-1h3.5c.6 0 1 .4 1 1 0 1.2.2 2.4.6 3.6.1.3 0 .7-.2 1z"/></svg>555-204-3187</span>
  <span><svg width="12" height="10" viewBox="0 0 24 18"><rect x="1" y="1" width="22" height="16" fill="none" stroke="#fff" stroke-width="2"/><path d="M1 1l11 9 11-9" fill="none" stroke="#fff" stroke-width="2"/></svg>orders@thornwickdelivery.com</span>
</div>

<header class="abs header">
  <div class="abs brand">THORNWICK DELIVERY</div>
  <div class="abs account">
    <span>LOG IN</span><span>REGISTER</span><span style="color:#aaa">|</span><span>YOUR CART &nbsp;0 ITMS</span>
  </div>
  <nav class="abs nav">
    <span class="active">HOME</span><span>ABOUT US</span><span>GROCERY ITEMS</span><span>HOW TO ORDER</span><span>CONTACT US</span>
  </nav>
</header>

<section class="abs hero" role="img" aria-label="Close-up photo of a burger with lettuce and fried food">
  <h1 class="abs center hero-title">THORNWICK FAST-FOOD RESTAURANTS</h1>
  <p class="abs center hero-sub">Thornwick Personal Grocery Shopping &amp; Delivery</p>
  <div class="abs btn-hero">VIEW DETAILS</div>
  <div class="abs dots"><i></i><i></i><i></i></div>
</section>

<h2 class="abs center sec-title" style="top:664px">WELCOME TO GROCERY ITEMS</h2>
<p class="abs intro">Thornwick Personal Grocery Shopping &amp; Delivery is a local, Thornwick-based company that delivers a broad assortment of all the grocery store products available for purchase from Thornwick area grocery stores such as Harlow Market and Pennyfield Foods.</p>

<div class="abs feature" style="left:115px;top:845px">
  <div class="icon"><svg width="56" height="60" viewBox="0 0 56 60"><path fill="#fff" d="M8 4h3v16h3V4h3v16h3V4h3v20c0 4-3 6-6 7v25h-6V31c-3-1-6-3-6-7zM40 4c6 0 9 10 9 22 0 5-3 7-5 7v23h-6V4z"/></svg></div>
  <h3>FRESH</h3>
  <p>Thornwick Personal Grocery Shopping &amp; Delivery is a local, Thornwick-based company that delivers a broad assortment of all the grocery store</p>
</div>
<div class="abs feature" style="left:449px;top:845px">
  <div class="icon"><svg width="62" height="42" viewBox="0 0 62 42"><path fill="#fff" d="M2 4h36v26H2zM40 12h11l9 11v7H40z"/><circle cx="13" cy="34" r="6" fill="#fff" stroke="#9c3f95" stroke-width="3"/><circle cx="49" cy="34" r="6" fill="#fff" stroke="#9c3f95" stroke-width="3"/></svg></div>
  <h3>FAST DELIVERY</h3>
  <p>Thornwick Personal Grocery Shopping &amp; Delivery is a local, Thornwick-based company that delivers a broad assortment of all the grocery store</p>
</div>
<div class="abs feature" style="left:783px;top:845px">
  <div class="icon"><svg width="60" height="44" viewBox="0 0 60 44"><rect x="3" y="3" width="54" height="38" rx="4" fill="none" stroke="#fff" stroke-width="4"/><rect x="3" y="12" width="54" height="7" fill="#fff"/><rect x="10" y="28" width="18" height="4" fill="#fff"/></svg></div>
  <h3>NO EXTRA CHARGES</h3>
  <p>Thornwick Personal Grocery Shopping &amp; Delivery is a local, Thornwick-based company that delivers a broad assortment of all the grocery store</p>
</div>

<section class="abs order-band">
  <h2 class="abs center sec-title" style="top:82px">HOW TO ORDER</h2>
  <div class="abs step" style="left:79px;top:184px">
    <div class="photo" role="img" aria-label="Photo of a family placing an order at home" style="background:radial-gradient(circle,#e8ddd0,#b9a48c)"></div>
    <h4>SUBMIT AN ORDER</h4>
  </div>
  <div class="abs step" style="left:449px;top:184px">
    <div class="photo" role="img" aria-label="Photo of a hand paying with a card on a laptop" style="background:radial-gradient(circle,#f0f0f0,#b8bcc2)"></div>
    <h4>CONFIRM YOUR ORDER</h4>
  </div>
  <div class="abs step" style="left:810px;top:184px">
    <div class="photo" role="img" aria-label="Photo of a delivery person carrying a crate of groceries" style="background:radial-gradient(circle,#c9b9a0,#5b6f8e)"></div>
    <h4>DELIVERY YOUR ORDER</h4>
  </div>
  <svg class="abs" style="left:0;top:0" width="1200" height="510" viewBox="0 0 1200 510">
    <path d="M330 340 C 400 360, 440 330, 478 300" fill="none" stroke="#222" stroke-width="3"/>
    <path d="M462 292 L490 292 L472 314 Z" fill="#222"/>
    <path d="M692 216 C 760 180, 820 210, 840 262" fill="none" stroke="#222" stroke-width="3"/>
    <path d="M826 262 L858 262 L840 280 Z" fill="#222"/>
  </svg>
</section>

<h2 class="abs center sec-title" style="top:1773px">FEATURED PRODUCTS</h2>
<svg class="abs" style="left:62px;top:1995px" width="26" height="50" viewBox="0 0 26 50"><path d="M22 2L4 25l18 23" fill="none" stroke="#333" stroke-width="2"/></svg>
<svg class="abs" style="left:1104px;top:1995px" width="26" height="50" viewBox="0 0 26 50"><path d="M4 2l18 23L4 48" fill="none" stroke="#333" stroke-width="2"/></svg>

<div class="abs product" style="left:132px;top:1881px">
  <div class="photo" role="img" aria-label="Product photo of a brown beer bottle" style="background:radial-gradient(ellipse at center,#f1e2d0 0%,#ffffff 50%,#e4e4e4 100%)"></div>
  <h5>BEER 12 PACKS</h5><div class="price">$18.49</div><div class="add">ADD TO CART</div>
</div>
<div class="abs product" style="left:372px;top:1881px">
  <div class="photo" role="img" aria-label="Product photo of a red wine bottle" style="background:radial-gradient(ellipse at center,#f6dcdf 0%,#ffffff 50%,#e4e4e4 100%)"></div>
  <h5>RED WINE</h5><div class="price">$18.49</div><div class="add">ADD TO CART</div>
</div>
<div class="abs product" style="left:612px;top:1881px">
  <div class="photo" role="img" aria-label="Product photo of an energy drink can" style="background:radial-gradient(ellipse at center,#e2d8cf 0%,#ffffff 50%,#e4e4e4 100%)"></div>
  <h5>ENERGY DRINK</h5><div class="price">$18.49</div><div class="add">ADD TO CART</div>
</div>
<div class="abs product" style="left:849px;top:1881px">
  <div class="photo" role="img" aria-label="Product photo of two e-cigarettes" style="background:radial-gradient(ellipse at center,#f4efe6 0%,#ffffff 50%,#e4e4e4 100%)"></div>
  <h5>E- CIGARETTES</h5><div class="price">$18.49</div><div class="add">ADD TO CART</div>
</div>

<footer class="abs footer">
  <div class="abs foot-brand">THORNWICK DELIVERY</div>
  <div class="abs social"><i></i><i></i><i></i><i></i><i></i></div>
  <div class="abs col" style="left:483px"><h6>QUICK LINKS</h6>
    <ul><li>Home</li><li>About Us</li><li>Grocery Items</li><li>How to Order</li><li>Contact us</li></ul></div>
  <div class="abs col" style="left:697px"><h6>COMPANY</h6>
    <ul><li>Shipping</li><li>Terms &amp; Conditions</li><li>Privacy</li><li>Site map</li><li>Track Order</li></ul></div>
  <div class="abs col" style="left:892px"><h6>CONTACT US</h6>
    <ul>
      <li><svg width="12" height="12" viewBox="0 0 24 24"><path fill="#555" d="M6.6 10.8a15 15 0 0 0 6.6 6.6l2.2-2.2c.3-.3.7-.4 1-.2 1.1.4 2.3.6 3.6.6.6 0 1 .4 1 1V20c0 .6-.4 1-1 1A17 17 0 0 1 3 4c0-.6.4-1 1-1h3.5c.6 0 1 .4 1 1 0 1.2.2 2.4.6 3.6.1.3 0 .7-.2 1z"/></svg>555-204-3187.</li>
      <li><svg width="12" height="12" viewBox="0 0 24 24"><rect x="5" y="2" width="14" height="7" fill="#555"/><rect x="2" y="9" width="20" height="9" fill="#555"/><rect x="6" y="15" width="12" height="7" fill="#555"/></svg>555-204-3187.</li>
      <li><svg width="12" height="10" viewBox="0 0 24 18"><rect x="0" y="0" width="24" height="18" fill="#555"/><path d="M1 1l11 9 11-9" fill="none" stroke="#fff" stroke-width="2"/></svg><span style="text-decoration:underline">orders@thornwickdelivery.com</span></li>
      <li style="align-items:flex-start;height:auto;line-height:16px;padding-top:4px"><svg width="10" height="14" viewBox="0 0 20 28"><path fill="#555" d="M10 0a10 10 0 0 0-10 10c0 7 10 18 10 18s10-11 10-18A10 10 0 0 0 10 0zm0 14a4 4 0 1 1 0-8 4 4 0 0 1 0 8z"/></svg><span>#2868 Lorem ipsum dolor sit<br>amet, consectetur</span></li>
    </ul></div>
</footer>
<div class="abs copyright">©2016 Thornwickdelivery.com. All Rights Reserved.</div>

</body>
</html>
```